Printing Business Card

I would like the colorful accents of my business to match with an artistic design. The idea is that I would like to have a creative mix so that I am making a embossed, suede card to show off with marketing events.

```html
<!DOCTYPE html>
<html lang="en">
<head>
<meta charset="utf-8">
<title>Keystone Print Co. – Business Card</title>
<link href="https://fonts.googleapis.com/css2?family=Poppins:wght@400;600&family=Kaushan+Script&display=swap" rel="stylesheet">
<style>
  :root {
    --stage: #2b2b2f;
    --card-black: #050505;
    --paper: #ffffff;
    --ink: #0a0a0a;
    --cyan: #27a7e0;
    --magenta: #e0217c;
    --yellow: #f2c81b;
    --text-light: #ffffff;
  }
  * { margin: 0; padding: 0; box-sizing: border-box; }
  html, body {
    width: 1200px; height: 801px; overflow: hidden;
    background: var(--stage);
    font-family: "Poppins", sans-serif;
  }
  .canvas {
    position: relative; width: 1200px; height: 801px;
    display: flex; align-items: center; justify-content: center; gap: 40px;
  }
  .card {
    position: relative; width: 520px; height: 297px;
    background: var(--card-black); overflow: hidden;
    box-shadow: 0 18px 40px rgba(0,0,0,.45);
  }
  .card-shapes { position: absolute; inset: 0; }

  .brand {
    position: absolute; display: flex; align-items: center; gap: 10px;
    font-family: "Poppins", sans-serif; font-weight: 600; font-size: 26px;
    white-space: nowrap;
  }
  .brand-dot { width: 14px; height: 14px; border-radius: 50%; }

  .card-front .brand { left: 50%; top: 50%; transform: translate(-50%, -50%); color: var(--text-light); }
  .card-front .brand-dot { background: var(--text-light); }

  .card-back .brand { left: 22px; top: 150px; font-size: 23px; color: var(--ink); }
  .card-back .brand-dot { background: var(--ink); }

  .contact {
    position: absolute; left: 345px; top: 44px; color: var(--text-light);
  }
  .contact-name {
    font-family: "Kaushan Script", cursive; font-size: 24px; line-height: 1.1;
  }
  .contact-role { font-size: 11px; margin-top: 2px; }
  .contact-address { font-size: 10.5px; line-height: 1.45; margin-top: 22px; }
  .contact-list { list-style: none; margin-top: 28px; font-size: 10.5px; }
  .contact-list li { display: flex; align-items: center; gap: 7px; line-height: 1.75; }
  .contact-list svg { width: 10px; height: 10px; flex: none; }
</style>
</head>
<body>
<main class="canvas">

  <section class="card card-front" aria-label="Business card front">
    <div class="brand"><span class="brand-dot"></span>Keystone Print Co.</div>
  </section>

  <section class="card card-back" aria-label="Business card back">
    <svg class="card-shapes" viewBox="0 0 520 297" aria-hidden="true">
      <defs><clipPath id="card-edge"><rect width="520" height="297"/></clipPath></defs>
      <g clip-path="url(#card-edge)" fill="none">
        <circle cx="100" cy="120" r="202" fill="var(--paper)"/>
        <path d="M306.2 102 A207 207 0 0 1 12.5 307.6" stroke="var(--yellow)" stroke-width="10"/>
        <path d="M315.2 101.2 A216 216 0 0 1 8.7 315.8" stroke="var(--magenta)" stroke-width="8"/>
        <path d="M322.2 100.6 A223 223 0 0 1 5.8 322.1" stroke="var(--cyan)" stroke-width="6"/>
      </g>
    </svg>

    <div class="brand"><span class="brand-dot"></span>Keystone Print Co.</div>

    <div class="contact">
      <p class="contact-name">Jordan Reyes</p>
      <p class="contact-role">Director</p>
      <p class="contact-address">PO BOX 456, Harbour Lane<br>7th street, Fairview</p>
      <ul class="contact-list">
        <li>
          <svg viewBox="0 0 10 10"><path d="M2 0.5 L4 3 L3 4 Q4 6 6 7 L7 6 L9.5 8 L8 9.5 Q3 9 0.5 2 Z" fill="currentColor"/></svg>
          +1 555 014 382
        </li>
        <li>
          <svg viewBox="0 0 10 10"><rect x="0.5" y="2" width="9" height="6" fill="currentColor"/><path d="M0.5 2 L5 5.5 L9.5 2" stroke="var(--card-black)" stroke-width="0.8" fill="none"/></svg>
          hello@keystoneprint.com
        </li>
        <li>
          <svg viewBox="0 0 10 10" fill="none" stroke="currentColor" stroke-width="0.9"><circle cx="5" cy="5" r="4.3"/><ellipse cx="5" cy="5" rx="2" ry="4.3"/><path d="M0.7 5 H9.3"/></svg>
          www.keystoneprint.com
        </li>
      </ul>
    </div>
  </section>

</main>
</body>
</html>
```